Fennick Executive Search - New Business Card Design Project

We are an executive search firm called Fennick Executive Search based in the UK. We require a custom design for a business card. We're looking to convey a professional service to executives for executive search recruitment services. In terms of colours, we like dark blues and grays (maybe even silver incorporated somewhere if we go for a foiled type of card) but we're open to your artistic flare. See our current logo in attachments. We are totally open on design so long as the design is slick and professional.
Updates

Thanks for all your contributions of various designs. I have to say the quality of work has been amazing which is going to make our job quite difficult in the coming days on making a decision. Thanks to you all that have taken the time to submit designs thus far. We'll keep on reviewing and try to narrow down our selection as soon as possible.

Target Market(s)

Executive Search

Industry/Entity Type

Recruitment

Contact Information for Business Card

Fennick Executive Search,
Exclusively Sourcing & Hiring Senior Leaders
Gordon Pellbury, Managing Director,
07823 906417
0117 486 7132
gordon@fennickexecutive.co.uk
fennickexecutive.co.uk
58 Lindmoor Court, Hatherley Road, Bristol, BS32 9QJ

Font styles to use
Sans Serif
Other font styles liked:
• Roboto (which is used in our logo)

Requirements
Must have
• Our logo (It has a subtle fade on it from #02071d at top to #333649 at bottom)
• The logo can be on one side or both sides
• Must be elegant and professional
• We have 2nd slogan CONSULT | INSPIRE | INNOVATE | DELIVER which can be incorporated into the card
Nice to have
• Use of blues and grey colours
• Compatible with similar styling to our website fennickexecutive.co.uk
Should not have
• Must not be overly brash
• Must not contain cartoon characters

```html
<!DOCTYPE html>
<html lang="en">
<head>
<meta charset="utf-8">
<title>Fennick Executive Search – Business Card</title>
<link rel="stylesheet" href="https://fonts.googleapis.com/css2?family=Arimo:wght@400;700&family=Tinos:wght@700&display=swap">
<style>
  :root {
    --backdrop: #999999;
    --card: #ffffff;
    --ink-purple: #3b2a7a;
    --rule-purple: #3a2680;
    --ink-grey: #555555;
    --label: #1f1f1f;
    --mark-ink: #1c1f33;
    --mark-square: #2a2d40;
  }
  * { margin: 0; padding: 0; box-sizing: border-box; }
  html, body { width: 1200px; height: 842px; overflow: hidden; }
  body {
    background: var(--backdrop);
    font-family: "Arimo", Arial, sans-serif;
    position: relative;
  }
  .card {
    position: absolute;
    width: 342px;
    height: 222px;
    background: var(--card);
    box-shadow: 4px 6px 8px rgba(0,0,0,0.35);
  }
  .card--front { left: 244px; top: 309px; }
  .card--back  { left: 614px; top: 311px; }

  .rule { position: absolute; background: var(--rule-purple); }
  .rule--h { height: 2px; }
  .rule--v { width: 2px; }

  .holder-name {
    position: absolute; right: 22px; top: 28px;
    font-family: "Tinos", "Times New Roman", serif;
    font-weight: 700; font-size: 19px; letter-spacing: 0.2px;
    color: var(--ink-purple); white-space: nowrap;
  }
  .holder-role {
    position: absolute; right: 22px; top: 53px;
    font-size: 8.6px; color: var(--ink-grey); letter-spacing: 0.3px;
  }
  .contact-icon { position: absolute; left: 9px; width: 20px; height: 20px; }
  .contact-block {
    position: absolute; left: 50px;
    font-size: 8.6px; line-height: 12.5px; color: var(--ink-purple);
    white-space: nowrap;
  }

  .company-mark {
    position: absolute;
    display: flex; align-items: center;
    font-weight: 700; color: var(--mark-ink);
    white-space: nowrap;
  }
  .company-mark__square { flex: none; background: var(--mark-square); }
  .card--front .company-mark { right: 14px; top: 168px; gap: 5px; font-size: 8px; line-height: 10px; }
  .card--front .company-mark__square { width: 20px; height: 20px; }
  .card--back .company-mark { left: 0; width: 342px; justify-content: center; top: 110px; gap: 8px; font-size: 13px; }
  .card--back .company-mark__square { width: 26px; height: 26px; }

  .tagline {
    position: absolute; left: 0; width: 342px; top: 154px;
    text-align: center; font-size: 9.4px; color: var(--ink-grey);
  }
  .web-address {
    position: absolute; right: 18px; top: 192px;
    font-size: 8.6px; color: var(--ink-grey);
  }
  .side-label {
    position: absolute; top: 570px; width: 200px;
    text-align: center; font-weight: 700; font-size: 12px;
    letter-spacing: 0.4px; color: var(--label);
  }
</style>
</head>
<body>

<section class="card card--front" aria-label="Business card front">
  <span class="rule rule--h" style="left:306px; top:14px; width:36px;"></span>
  <span class="rule rule--v" style="left:329px; top:1px; height:78px;"></span>
  <span class="rule rule--v" style="left:36px; top:75px; height:143px;"></span>
  <span class="rule rule--h" style="left:0; top:209px; width:74px;"></span>

  <h1 class="holder-name">GORDON PELLBURY</h1>
  <p class="holder-role">MANAGING DIRECTOR</p>

  <svg class="contact-icon" style="top:107px" viewBox="0 0 20 20" aria-label="Address">
    <circle cx="10" cy="10" r="10" fill="var(--rule-purple)"/>
    <path d="M5 10.5 L10 6 L15 10.5 M6.8 9.5 V14 H13.2 V9.5" fill="none" stroke="#fff" stroke-width="1.4"/>
  </svg>
  <svg class="contact-icon" style="top:139px" viewBox="0 0 20 20" aria-label="Email">
    <circle cx="10" cy="10" r="10" fill="var(--rule-purple)"/>
    <rect x="5" y="6.5" width="10" height="7" fill="none" stroke="#fff" stroke-width="1.2"/>
    <path d="M5 6.5 L10 10.5 L15 6.5" fill="none" stroke="#fff" stroke-width="1.2"/>
  </svg>
  <svg class="contact-icon" style="top:171px" viewBox="0 0 20 20" aria-label="Phone">
    <circle cx="10" cy="10" r="10" fill="var(--rule-purple)"/>
    <path d="M7 5 L9 5 L9.6 7.6 L8.4 8.6 Q9.6 11.2 11.6 12 L12.6 10.8 L15 11.4 L15 13.4 Q14 15 12 14.6 Q6.4 12.6 5.4 7 Q5.4 5.4 7 5 Z" fill="#fff"/>
  </svg>

  <p class="contact-block" style="top:104px">58 Lindmoor Court, Hatherley Road, Bristol,<br>&nbsp;BS32 9QJ</p>
  <p class="contact-block" style="top:139px">gordon@fennickexecutive.co.uk<br>fennickexecutive.co.uk</p>
  <p class="contact-block" style="top:171px">07823 906417<br>0117 486 7132</p>

  <div class="company-mark">
    <span class="company-mark__square"></span>
    <span>Fennick<br>Executive Search</span>
  </div>
</section>

<section class="card card--back" aria-label="Business card back">
  <span class="rule rule--h" style="left:11px; top:11px; width:200px;"></span>
  <span class="rule rule--v" style="left:20px; top:3px; height:99px;"></span>
  <span class="rule rule--v" style="left:328px; top:106px; height:104px;"></span>
  <span class="rule rule--h" style="left:131px; top:207px; width:209px;"></span>

  <div class="company-mark">
    <span class="company-mark__square"></span>
    <span>Fennick Executive Search</span>
  </div>
  <p class="tagline">Exclusively Sourcing &amp; Hiring Senior Leaders</p>
  <p class="web-address">www.fennickexecutive.co.uk</p>
</section>

<p class="side-label" style="left:326px">FRONT SIDE</p>
<p class="side-label" style="left:677px">BACK SIDE</p>

</body>
</html>
```